Small 3.5x7.5 Book Flyer Need some Design Work

I have the concept and the pictures just need some flair to make it look good.

Basically we want to advertise our product is the same as the dealer product for a much less price. ITs the same thing. maybe says ELIMINATE THE MIDDLEMAN or SAVE MONEY BUYING DIRECT. The BRANDS we sell are DORNSHAWLEY , BRAKU , NOLAQ , PARVIN, HENDARO. The types of machines we sell parts for are ARTICULATED TRUCKS, RIGID FRAME TRUCKS (Those two can be grouped together ARTICULATED/RIGID if room is needed), WHEEL LOADERS, COMPACTORS, SCRAPERS. The types of products we sell are TRANSMISSIONS, DIFFERENTIALS, FINAL DRIVES, BRAKES, CYLINDERS, and NEW PARTS. This should be somewhere to read on their, dont care wear but looks nice.

This needs to be 3.5" (Width) 7.5 " Height. See deign concept. INcluded log and picture of the part to feature.

Target Market(s)

Rock Quarries, Aggregate PRoducers, Construction companies

Industry/Entity Type

Product

Font styles to use
Sans Serif

Colors
ffffff
000000
fbed22

Requirements
Must have
• The bottom should have our logo and phone number 555-017-3248, website http://www.drobtrade.com (you can also see brenvoxtrailco.com for an understanding of what we sell and more pictures). Address: 718 Pellham Row Tamsford NE 58317
Nice to have
• I put OURS and THEIRS, but I think now it should be OURS - FACTORY
• And maybe shows that both components include:
• NEW OEM SEALS
• NEW OEM GASKETS
• NEW OEM BEARINGS
• NEW OEM FRICTIONS
• NEW OEM PLATES
• NEW OEM SOLENOIDS
• REBUILT / BALANCED TORQUE CONVERTER
• It would show these things on the side maybe, on both transmissions - basically showing that ours is exactly the same as the factories but a fraction of the cost.
• Maybe we dont need the price tag. Just show all of those things the same and the bottom line after torque converter would be the PRICE in different color so it stands out.

```html
<!DOCTYPE html>
<html lang="en">
<head>
<meta charset="utf-8">
<title>Drobtrade Industrial – Why Spend More</title>
<link href="https://fonts.googleapis.com/css2?family=Black+Ops+One&family=Archivo+Black&family=Oswald:wght@400;500&family=Source+Sans+3:wght@400;600;700&family=Montserrat:wght@700;800&display=swap" rel="stylesheet">
<style>
  :root {
    --black: #000000;
    --white: #ffffff;
    --yellow: #fbed22;
    --stencil-yellow: #f3e62a;
    --metal-light: #b9bcbd;
    --metal-dark: #55595b;
    --price-red: #e3222b;
    --price-green: #1d8f4e;
    --pill-dark: #222222;
    --rule-red: #d4262b;
  }
  * { margin: 0; padding: 0; box-sizing: border-box; }
  html, body { width: 1200px; height: 2571px; overflow: hidden; background: var(--black); }
  .flyer {
    position: relative; width: 1200px; height: 2571px; overflow: hidden;
    background: radial-gradient(ellipse at 50% 35%, #3a3a3a 0%, #1c1c1c 55%, #0d0d0d 100%);
    font-family: "Source Sans 3", sans-serif; color: var(--white);
  }
  .brand-mark {
    position: absolute; top: 95px; left: 0; width: 100%;
    display: flex; justify-content: center; align-items: center; gap: 32px;
  }
  .brand-mark .dot { width: 120px; height: 120px; border-radius: 50%; background: var(--white); }
  .brand-mark .name {
    font-family: "Montserrat", sans-serif; font-weight: 800; font-size: 84px;
    line-height: 1; color: var(--white); letter-spacing: 2px;
  }
  .headline {
    position: absolute; top: 372px; width: 100%; text-align: center; white-space: nowrap;
    font-family: "Black Ops One", sans-serif; font-size: 96px; line-height: 1;
    color: var(--stencil-yellow); letter-spacing: 0;
  }
  .features {
    position: absolute; top: 596px; list-style: none;
    font-size: 34px; line-height: 47px; font-weight: 400; color: var(--white);
  }
  .features.left { left: 162px; }
  .features.right { left: 656px; }
  .features li { position: relative; padding-left: 50px; white-space: nowrap; }
  .features li svg { position: absolute; left: 0; top: 10px; width: 30px; height: 30px; }
  .part-photo { position: absolute; border-radius: 40px; }
  .part-photo.ours {
    left: 86px; top: 889px; width: 620px; height: 504px;
    background: linear-gradient(160deg, var(--metal-light) 0%, #8d9192 45%, var(--metal-dark) 100%);
  }
  .part-photo.factory {
    left: 750px; top: 911px; width: 375px; height: 321px;
    background: linear-gradient(160deg, var(--metal-light) 0%, #8d9192 45%, var(--metal-dark) 100%);
  }
  .pill {
    position: absolute; display: flex; align-items: center; white-space: nowrap;
    font-family: "Source Sans 3", sans-serif; font-weight: 700; color: var(--white);
  }
  .label-factory {
    left: 771px; top: 1212px; width: 360px; height: 44px; padding-left: 16px;
    background: var(--pill-dark); border-radius: 22px; font-size: 28px; letter-spacing: 1px;
  }
  .price-factory {
    left: 771px; top: 1254px; width: 188px; height: 58px; justify-content: center;
    background: var(--price-red); border-radius: 29px; font-size: 44px;
  }
  .label-ours {
    left: 139px; top: 1374px; width: 488px; height: 62px; padding-left: 36px;
    background: var(--pill-dark); border-radius: 31px; font-size: 42px;
  }
  .price-ours {
    left: 139px; top: 1436px; width: 294px; height: 96px; justify-content: center;
    background: var(--price-green); border-radius: 48px; font-size: 70px;
  }
  .info-band {
    position: absolute; left: 0; top: 1611px; width: 100%; height: 960px; background: var(--black);
  }
  .brand-list {
    position: absolute; top: 1648px; width: 100%; text-align: center; white-space: nowrap;
    font-family: "Archivo Black", sans-serif; font-size: 31px; color: var(--yellow); letter-spacing: 1px;
  }
  .section-title {
    position: absolute; width: 100%; text-align: center;
    font-family: "Oswald", sans-serif; font-weight: 400; font-size: 38px; color: var(--white);
  }
  .section-title span { display: inline-block; border-bottom: 4px solid var(--rule-red); padding-bottom: 2px; line-height: 1.1; }
  .products-title { top: 1756px; }
  .niche-title { top: 1923px; }
  .section-body {
    position: absolute; width: 100%; text-align: center;
    font-family: "Oswald", sans-serif; font-weight: 400; font-size: 28px; line-height: 39px;
    color: var(--white);
  }
  .products-body { top: 1819px; }
  .niche-body { top: 1985px; }
  .contact-dome { position: absolute; left: 0; top: 2110px; width: 1200px; height: 461px; }
  .contact { position: absolute; width: 100%; text-align: center; color: var(--black); white-space: nowrap; }
  .contact.web { top: 2220px; font-family: "Source Sans 3", sans-serif; font-weight: 700; font-size: 62px; }
  .contact.address { top: 2312px; font-family: "Source Sans 3", sans-serif; font-weight: 400; font-size: 48px; }
  .contact.phone { top: 2390px; font-family: "Archivo Black", sans-serif; font-size: 120px; letter-spacing: 2px; }
</style>
</head>
<body>
<div class="flyer">
  <div class="brand-mark">
    <span class="dot"></span>
    <span class="name">DROBTRADE</span>
  </div>

  <div class="headline">WHY SPEND MORE</div>

  <ul class="features left">
    <li><svg viewBox="0 0 30 30"><circle cx="15" cy="15" r="12" fill="none" stroke="#fbed22" stroke-width="2.5"/><path d="M9 15l4 4 9-10" fill="none" stroke="#fbed22" stroke-width="3"/></svg>NEW OEM SEALS</li>
    <li><svg viewBox="0 0 30 30"><circle cx="15" cy="15" r="12" fill="none" stroke="#fbed22" stroke-width="2.5"/><path d="M9 15l4 4 9-10" fill="none" stroke="#fbed22" stroke-width="3"/></svg>NEW OEM GASKETS</li>
    <li><svg viewBox="0 0 30 30"><circle cx="15" cy="15" r="12" fill="none" stroke="#fbed22" stroke-width="2.5"/><path d="M9 15l4 4 9-10" fill="none" stroke="#fbed22" stroke-width="3"/></svg>NEW OEM BEARINGS</li>
    <li><svg viewBox="0 0 30 30"><circle cx="15" cy="15" r="12" fill="none" stroke="#fbed22" stroke-width="2.5"/><path d="M9 15l4 4 9-10" fill="none" stroke="#fbed22" stroke-width="3"/></svg>NEW OEM FRICTIONS</li>
  </ul>
  <ul class="features right">
    <li><svg viewBox="0 0 30 30"><circle cx="15" cy="15" r="12" fill="none" stroke="#fbed22" stroke-width="2.5"/><path d="M9 15l4 4 9-10" fill="none" stroke="#fbed22" stroke-width="3"/></svg>NEW OEM PLATES</li>
    <li><svg viewBox="0 0 30 30"><circle cx="15" cy="15" r="12" fill="none" stroke="#fbed22" stroke-width="2.5"/><path d="M9 15l4 4 9-10" fill="none" stroke="#fbed22" stroke-width="3"/></svg>NEW OEM SOLENOIDS</li>
    <li><svg viewBox="0 0 30 30"><circle cx="15" cy="15" r="12" fill="none" stroke="#fbed22" stroke-width="2.5"/><path d="M9 15l4 4 9-10" fill="none" stroke="#fbed22" stroke-width="3"/></svg>REBUILT / BALANCED</li>
    <li>TORQUE CONVERTER</li>
  </ul>

  <div class="part-photo ours" role="img" aria-label="Photo of the rebuilt transmission offered by Drobtrade"></div>
  <div class="part-photo factory" role="img" aria-label="Photo of the factory dealer transmission"></div>

  <div class="pill label-factory">FACTORY COMPONENT</div>
  <div class="pill price-factory">$35,900</div>
  <div class="pill label-ours">OUR COMPONENT</div>
  <div class="pill price-ours">$19,800</div>

  <div class="info-band"></div>
  <div class="brand-list">DORNSHAWLEY | BRAKU | NOLAQ | PARVIN | HENDARO</div>

  <div class="section-title products-title"><span>OUR PRODUCTS</span></div>
  <div class="section-body products-body">TRANSMISSIONS, DIFFERENTIALS, FINAL DRIVES,<br>BRAKES, CYLINDERS, and NEW PARTS</div>

  <div class="section-title niche-title"><span>OUR NICHE</span></div>
  <div class="section-body niche-body">ARTICULATED TRUCKS, RIGID FRAME TRUCKS,<br>WHEEL LOADERS, COMPACTORS, SCRAPERS.</div>

  <svg class="contact-dome" viewBox="0 0 1200 461" preserveAspectRatio="none" aria-hidden="true">
    <path d="M0 461 L0 170 Q600 -170 1200 170 L1200 461 Z" fill="#fbed22"/>
  </svg>
  <div class="contact web">www.drobtrade.com</div>
  <div class="contact address">718 Pellham Row Tamsford NE 58317</div>
  <div class="contact phone">555-017-3248</div>
</div>
</body>
</html>
```